BRIGHT FERN STUDIO photography made affordable

Photography made simple and affordable i provide back drop photography baby photography and childrens cake smash photography we also offer a range of back drops at a guaranteed affordable price we are a pop up studio we are a family owned business and we pride oursleves on making proffesional photography affordable for the average house hold we offer a variety of packages ranging from minis too larger values we are here to bring your memories to images for you too have forever and cherish

Target Market(s)

Baby photography portrait shots cake smash

Industry/Entity Type

Photography

Contact Information for Business Card

phone number 0417529864 EMAIL brightfernstudio@pixelmail.net

Font styles to use
Decorative

Requirements
Must have
• A professional look
Nice to have
• Simple but eye catching

```html
<!DOCTYPE html>
<html lang="en">
<head>
<meta charset="utf-8">
<title>Bright Fern Studio – Business Card Set</title>
<link href="https://fonts.googleapis.com/css2?family=Lato:wght@400;700;900&display=swap" rel="stylesheet">
<style>
  :root{
    --board:#acacac;
    --card-white:#ffffff;
    --brand-blue:#3456b0;
    --back-blue:#3a5fb7;
    --back-blue-deep:#2f50a6;
    --ink:#111111;
    --label:#141414;
    --photo-frame:#ffffff;
  }
  *{margin:0;padding:0;box-sizing:border-box}
  html,body{width:1200px;height:1114px;overflow:hidden;background:var(--board)}
  body{position:relative;font-family:'Lato',Arial,sans-serif}

  .card{position:absolute;width:438px;height:250px;border-radius:14px;overflow:hidden}
  .card--front{left:110px;background:var(--card-white)}
  .card--back{left:645px;background:var(--back-blue)}
  .row-1{top:99px}.row-2{top:409px}.row-3{top:719px}

  .card-label{position:absolute;width:438px;text-align:center;font-size:20px;color:var(--label);letter-spacing:.2px}
  .card-label--front{left:110px}.card-label--back{left:645px}

  .brand-stack{position:absolute;left:24px;top:76px;color:var(--brand-blue);font-weight:900;font-size:22px;line-height:22px;letter-spacing:.5px}
  .owner-name{position:absolute;left:24px;top:168px;color:var(--brand-blue);font-weight:700;font-size:19px}
  .contact{position:absolute;left:24px;display:flex;align-items:center;gap:5px;color:var(--ink)}
  .contact--phone{top:198px;font-size:14px;font-weight:700;letter-spacing:.4px}
  .contact--email{top:216px;font-size:9.5px}
  .contact svg{flex:none}

  .print{position:absolute;background:var(--photo-frame);padding:5px;box-shadow:0 1px 4px rgba(0,0,0,.25)}
  .print .shot{width:100%;height:100%}
  .print--portrait{padding:0;box-shadow:none}
  .tone-star{background:linear-gradient(160deg,#1f3170,#2c3f86 50%,#c9b8a0)}
  .tone-jacket{background:linear-gradient(180deg,#cfd3d9 0%,#7a4a36 45%,#5b3326 100%)}
  .tone-snow{background:linear-gradient(170deg,#7f8a9a,#e9e4dc 55%,#d8cfc2)}
  .tone-snowbaby{background:linear-gradient(160deg,#c9cdd3,#8a4b36 50%,#ece7df)}
  .tone-orange-star{background:linear-gradient(160deg,#2c3650,#3f4a66 55%,#c49a84)}

  .back-photo{position:absolute;inset:0}
  .back-photo--snow{background:radial-gradient(ellipse at 50% 45%,#4a6cc0 0%,var(--back-blue) 55%,var(--back-blue-deep) 100%)}
  .back-photo--stars{background:radial-gradient(ellipse at 50% 80%,#4668bd 0%,var(--back-blue-deep) 70%)}
  .back-photo--baby{background:linear-gradient(110deg,#3353a8 0%,var(--back-blue) 45%,#4468bd 100%)}
  .back-brand{position:absolute;left:0;right:0;top:100px;text-align:center;color:#fff;font-weight:900;font-size:33px;letter-spacing:1.5px}
</style>
</head>
<body>

<!-- Row 1 -->
<section class="card card--front row-1">
  <div class="brand-stack">BRIGHT<br>FERN<br>STUDIO</div>
  <div class="owner-name">Lena Hartwell</div>
  <div class="contact contact--phone"><svg width="9" height="9" viewBox="0 0 24 24"><path fill="#3456b0" d="M6.6 10.8a15 15 0 006.6 6.6l2.2-2.2a1 1 0 011-.25 11.4 11.4 0 003.6.57 1 1 0 011 1V20a1 1 0 01-1 1A17 17 0 013 4a1 1 0 011-1h3.5a1 1 0 011 1c0 1.25.2 2.45.57 3.6a1 1 0 01-.25 1z"/></svg>0417529864</div>
  <div class="contact contact--email"><svg width="9" height="7" viewBox="0 0 24 18"><rect width="24" height="18" rx="2" fill="#3456b0"/><path d="M2 2l10 8 10-8" stroke="#fff" stroke-width="2" fill="none"/></svg>brightfernstudio@pixelmail.net</div>
  <div class="print print--portrait" style="left:223px;top:30px;width:122px;height:157px"><div class="shot tone-jacket" role="img" aria-label="Portrait of a baby in a quilted brown jacket"></div></div>
  <div class="print" style="left:160px;top:73px;width:115px;height:150px;transform:rotate(-21deg)"><div class="shot tone-star" role="img" aria-label="Baby in front of a starry blue backdrop"></div></div>
  <div class="print" style="left:330px;top:128px;width:85px;height:95px;transform:rotate(20deg)"><div class="shot tone-snowbaby" role="img" aria-label="Baby sitting beside a snowman toy"></div></div>
</section>
<div class="card-label card-label--front" style="top:366px">FRONT CARD 01</div>

<section class="card card--back row-1">
  <div class="back-photo back-photo--snow" role="img" aria-label="Faint snowman backdrop under a blue wash"></div>
  <div class="back-brand">BRIGHT FERN STUDIO</div>
</section>
<div class="card-label card-label--back" style="top:366px">BACK CARD 01</div>

<!-- Row 2 -->
<section class="card card--front row-2">
  <div class="brand-stack">BRIGHT<br>FERN<br>STUDIO</div>
  <div class="owner-name">Lena Hartwell</div>
  <div class="contact contact--phone"><svg width="9" height="9" viewBox="0 0 24 24"><path fill="#3456b0" d="M6.6 10.8a15 15 0 006.6 6.6l2.2-2.2a1 1 0 011-.25 11.4 11.4 0 003.6.57 1 1 0 011 1V20a1 1 0 01-1 1A17 17 0 013 4a1 1 0 011-1h3.5a1 1 0 011 1c0 1.25.2 2.45.57 3.6a1 1 0 01-.25 1z"/></svg>0417529864</div>
  <div class="contact contact--email"><svg width="9" height="7" viewBox="0 0 24 18"><rect width="24" height="18" rx="2" fill="#3456b0"/><path d="M2 2l10 8 10-8" stroke="#fff" stroke-width="2" fill="none"/></svg>brightfernstudio@pixelmail.net</div>
  <div class="print print--portrait" style="left:223px;top:30px;width:122px;height:157px"><div class="shot tone-jacket" role="img" aria-label="Portrait of a baby in a quilted brown jacket"></div></div>
  <div class="print" style="left:160px;top:73px;width:115px;height:150px;transform:rotate(-21deg)"><div class="shot tone-star" role="img" aria-label="Baby in front of a starry blue backdrop"></div></div>
  <div class="print" style="left:330px;top:123px;width:85px;height:100px;transform:rotate(20deg)"><div class="shot tone-snow" role="img" aria-label="Close-up of a snowman toy"></div></div>
</section>
<div class="card-label card-label--front" style="top:676px">FRONT CARD 02</div>

<section class="card card--back row-2">
  <div class="back-photo back-photo--stars" role="img" aria-label="Faint starry backdrop with a baby under a blue wash"></div>
  <div class="back-brand">BRIGHT FERN STUDIO</div>
</section>
<div class="card-label card-label--back" style="top:676px">BACK CARD 02</div>

<!-- Row 3 -->
<section class="card card--front row-3">
  <div class="brand-stack">BRIGHT<br>FERN<br>STUDIO</div>
  <div class="owner-name">Lena Hartwell</div>
  <div class="contact contact--phone"><svg width="9" height="9" viewBox="0 0 24 24"><path fill="#3456b0" d="M6.6 10.8a15 15 0 006.6 6.6l2.2-2.2a1 1 0 011-.25 11.4 11.4 0 003.6.57 1 1 0 011 1V20a1 1 0 01-1 1A17 17 0 013 4a1 1 0 011-1h3.5a1 1 0 011 1c0 1.25.2 2.45.57 3.6a1 1 0 01-.25 1z"/></svg>0417529864</div>
  <div class="contact contact--email"><svg width="9" height="7" viewBox="0 0 24 18"><rect width="24" height="18" rx="2" fill="#3456b0"/><path d="M2 2l10 8 10-8" stroke="#fff" stroke-width="2" fill="none"/></svg>brightfernstudio@pixelmail.net</div>
  <div class="print" style="left:176px;top:15px;width:74px;height:88px;transform:rotate(12deg)"><div class="shot tone-snow" role="img" aria-label="Close-up of a snowman toy"></div></div>
  <div class="print print--portrait" style="left:244px;top:30px;width:101px;height:157px"><div class="shot tone-jacket" role="img" aria-label="Portrait of a baby in a quilted brown jacket"></div></div>
  <div class="print" style="left:336px;top:50px;width:62px;height:72px;transform:rotate(-20deg)"><div class="shot tone-snowbaby" role="img" aria-label="Baby sitting beside a snowman toy"></div></div>
  <div class="print" style="left:166px;top:110px;width:100px;height:115px;transform:rotate(-20deg)"><div class="shot tone-orange-star" role="img" aria-label="Smiling baby in front of an orange star backdrop"></div></div>
  <div class="print" style="left:330px;top:123px;width:84px;height:100px;transform:rotate(20deg)"><div class="shot tone-star" role="img" aria-label="Baby in front of a starry blue backdrop"></div></div>
</section>
<div class="card-label card-label--front" style="top:986px">FRONT CARD 03</div>

<section class="card card--back row-3">
  <div class="back-photo back-photo--baby" role="img" aria-label="Faint baby and snowman under a blue wash"></div>
  <div class="back-brand">BRIGHT FERN STUDIO</div>
</section>
<div class="card-label card-label--back" style="top:986px">BACK CARD 03</div>

</body>
</html>
```